Web Page for marketing online agency

We are an online marketing agency that is acing the direct response model. We engage with our customers throughout different marketing techniques as research copy-writing, advertisements and content writing. We would need a website design that will have four main aspects: The Vision; stating who we are, The Mission; stating what we do, The Team And It's Values, and a Contact Form. For this design we would want a sharp, clean and smart approach, with illustrated elements or suggestive images. You can use the attached copy, the logo, the USP and the motto. Please integrate them as you see fit while keeping in mind the previous needs and copy. This website is going to be our connection with our possible partners, future colleagues and even our clients. You may submit a design for one page or integrate the 4 different aspects on separate web pages.
Target Market(s)
business partners, future employees, age range 25-60
Industry/Entity Type
Direct Marketing
Number of Pages Required
1 page
Requirements
Must have
- Menu / Header
- 4 Parts or 4 Pages including: vision, mission, team, contact
- Logo
- Motto: Direct Brilliance
- USP: We help people help themselves.
- The copy attached
Nice to have
- Representative illustrated images or elements
Should not have
- A boring design, classical design - WordPress like

```html
<!DOCTYPE html>
<html lang="en">
<head>
<meta charset="utf-8">
<title>BrightLeaf – Direct Brilliance</title>
<link rel="stylesheet" href="https://fonts.googleapis.com/css2?family=Lato:wght@300;400;700&display=swap">
<style>
:root{
  --blue:#35aee2;
  --blue-dark:#1f8fc8;
  --ink:#3a3a3a;
  --text:#5b5b5b;
  --muted:#8a8a8a;
  --white:#ffffff;
  --footer:#2e2e2e;
  --team-bg:#3d3f44;
}
*{box-sizing:border-box;margin:0;padding:0}
html,body{width:1200px;height:3243px;overflow:hidden;background:var(--white)}
body{font-family:'Lato',sans-serif;color:var(--text);position:relative}
.abs{position:absolute}
.center{text-align:center}

/* header */
.site-header{position:absolute;left:0;top:0;width:1200px;height:125px;background:var(--white)}
.brand{position:absolute;left:78px;top:48px;display:flex;align-items:center;gap:10px;font-size:46px;font-weight:700;color:var(--ink);line-height:1}
.brand-dot{width:22px;height:22px;border-radius:50%;background:var(--blue);margin-top:-36px}
.main-nav a{position:absolute;top:55px;font-size:17px;color:#8a8a8a;text-decoration:none;letter-spacing:.3px}
.main-nav a.active{color:var(--blue)}

/* hero */
.hero{position:absolute;left:0;top:125px;width:1200px;height:552px;
  background:linear-gradient(135deg,#d9dde2 0%,#eef0f2 40%,#c9d3dc 70%,#e7eaee 100%)}
.hero-veil{position:absolute;inset:0;background:rgba(255,255,255,.45)}
.hero h1{position:absolute;left:0;width:1200px;top:205px;font-size:48px;font-weight:700;color:#3b3b3b;text-align:center}
.hero p{position:absolute;left:320px;width:560px;top:282px;font-size:16px;line-height:28px;color:#3f3f3f;text-align:center}

/* section titles */
.section-title{position:absolute;left:0;width:1200px;text-align:center;font-size:42px;font-weight:700;color:#555}
.section-lead{position:absolute;left:230px;width:740px;text-align:center;font-size:15px;line-height:26px;color:#666}

/* who we are */
.value-label{position:absolute;font-size:16px;color:#666}
.value-ring{position:absolute;left:190px;top:870px}
.value-list{position:absolute;left:625px;top:872px;width:490px;list-style:none}
.value-list li{position:relative;padding-left:32px;font-size:14px;line-height:25px;color:#666;margin-bottom:14px}
.value-list li::before{content:"";position:absolute;left:0;top:6px;width:16px;height:16px;border-radius:50%;background:var(--blue)}
.btn{position:absolute;display:flex;align-items:center;justify-content:center;width:166px;height:41px;border-radius:21px;background:var(--blue);color:var(--white);font-size:17px;font-weight:700;text-decoration:none}

/* what we do */
.services{position:absolute;left:0;top:1250px;width:1200px;height:523px;background:var(--blue)}
.services .section-title{color:var(--white);top:48px}
.services .section-lead{color:var(--white);top:108px}
.service-link{position:absolute;left:360px;top:279px;width:480px;height:10px}
.service-icon{position:absolute;top:211px;width:144px;height:144px;border-radius:50%;border:3px solid rgba(255,255,255,.8);display:flex;align-items:center;justify-content:center}
.service-icon span{width:124px;height:124px;border-radius:50%;background:var(--white);display:flex;align-items:center;justify-content:center}
.service-text{position:absolute;top:380px;width:300px;text-align:center;color:var(--white);font-size:15px;line-height:27px}

/* team */
.team{position:absolute;left:0;top:1773px;width:1200px;height:584px;
  background:linear-gradient(160deg,#55595f 0%,#3a3c40 45%,#4a4c50 75%,#2f3033 100%)}
.team .section-title{color:var(--white);top:50px}
.team .section-lead{color:var(--white);top:107px;left:230px;width:740px}
.team-grid{position:absolute;left:78px;top:210px;width:1046px;height:290px}
.value-cell{position:absolute;width:349px;text-align:center;color:var(--white)}
.value-cell h3{font-size:22px;font-weight:400;margin-bottom:8px}
.value-cell p{font-size:14px;line-height:24px;color:#e6e6e6;padding:0 20px}
.grid-line{position:absolute;background:rgba(255,255,255,.35)}

/* leaders */
.leader-photo{position:absolute;width:94px;height:94px;border-radius:50%;border:3px solid var(--blue);
  background:radial-gradient(circle at 50% 40%,#c9b6a4 0%,#6d5a4d 60%,#2e2b2a 100%)}
.leader-name{position:absolute;font-size:21px;font-weight:700;color:#4a4a4a}
.leader-role{position:absolute;font-size:16px;color:#777}
.leader-bio{position:absolute;width:490px;font-size:14px;line-height:23px;color:#666}

/* contact */
.contact{position:absolute;left:0;top:2804px;width:1200px;height:374px;background:var(--blue)}
.contact-card{position:absolute;left:78px;top:54px;width:307px;height:244px;border:2px solid rgba(255,255,255,.75);color:var(--white)}
.contact-card h3{position:absolute;left:22px;top:34px;font-size:25px;font-weight:700}
.contact-row{position:absolute;left:22px;display:flex;gap:16px;font-size:15px;line-height:24px}
.contact-row svg{flex:none;margin-top:3px}
.contact h2{position:absolute;left:452px;top:58px;font-size:40px;font-weight:700;color:var(--white)}
.field{position:absolute;border:1.5px solid rgba(255,255,255,.85);color:rgba(255,255,255,.9);font-size:14px;font-style:italic;padding:9px 12px}
.send{position:absolute;left:1059px;top:132px;width:63px;height:145px;background:var(--white);display:flex;align-items:center;justify-content:center}

.site-footer{position:absolute;left:0;top:3178px;width:1200px;height:65px;background:var(--footer);color:#ddd;font-size:15px;display:flex;align-items:center;justify-content:center}
</style>
</head>
<body>

<header class="site-header">
  <div class="brand"><span>BrightLeaf</span><span class="brand-dot"></span></div>
  <nav class="main-nav">
    <a class="active" href="#" style="left:581px">HOME</a>
    <a href="#" style="left:671px">ABOUT</a>
    <a href="#" style="left:768px">WHAT WE DO</a>
    <a href="#" style="left:919px">OUR TEAM</a>
    <a href="#" style="left:1043px">CONTACT</a>
  </nav>
</header>

<section class="hero" role="img" aria-label="Photo of people working together at a laptop">
  <div class="hero-veil"></div>
  <h1>We help people help themselves.</h1>
  <p>We are a direct response company that creates and sells information products and services that millions of people find interesting and important in their lives.</p>
</section>

<section class="vision">
  <h2 class="section-title" style="top:722px">Who We &nbsp;Are</h2>
  <p class="section-lead" style="top:782px;left:240px;width:720px">We are a direct response company that creates and sells information products and services that millions of people find interesting and important in their lives.</p>

  <svg class="value-ring" width="270" height="290" viewBox="0 0 270 290">
    <defs>
      <linearGradient id="ringGrad" x1="0" y1="0" x2="0" y2="1">
        <stop offset="0" stop-color="#5cc3ee"/>
        <stop offset="1" stop-color="#1a8bd0"/>
      </linearGradient>
    </defs>
    <circle cx="130" cy="142" r="101" fill="none" stroke="url(#ringGrad)" stroke-width="36"/>
    <g fill="#fff" stroke="#e2e2e2" stroke-width="2">
      <circle cx="63" cy="32" r="26"/>
      <circle cx="221" cy="34" r="26"/>
      <circle cx="18" cy="172" r="26"/>
      <circle cx="253" cy="170" r="26"/>
      <circle cx="134" cy="252" r="26"/>
    </g>
    <g fill="none" stroke="#9a9a9a" stroke-width="2" stroke-linecap="round">
      <path d="M63 20v24M52 26h22M52 26l-5 10h10zM74 26l-5 10h10zM57 44h12"/>
      <path d="M221 44c-10-7-14-11-14-16a6 6 0 0 1 14-2 6 6 0 0 1 14 2c0 5-4 9-14 16z"/>
      <path d="M10 178c4 4 12 4 16 0M18 162v8M12 166h12"/>
      <path d="M247 164c0-6 12-6 12 0v8c0 5-12 5-12 0z"/>
      <path d="M134 240l10 4v8c0 6-5 10-10 12-5-2-10-6-10-12v-8zM129 252l4 4 6-7"/>
    </g>
  </svg>
  <span class="value-label" style="left:135px;top:890px">Fairness</span>
  <span class="value-label" style="left:461px;top:892px">Freedom</span>
  <span class="value-label" style="left:110px;top:1032px">Caring</span>
  <span class="value-label" style="left:488px;top:1032px">Safety</span>
  <span class="value-label" style="left:250px;top:1164px">Unconditioned help</span>

  <ul class="value-list">
    <li>We are specialized in the self-reliance market and we serve conservative Americans.</li>
    <li>We are in this business to serve globally and to grow individually.</li>
    <li>What we serve and inspire are people who need safety, comfort and peace of mind.</li>
    <li>We deliver empowerment through products that create fertile shortcuts to solutions, disentangle reality, simplify choices and ultimately make lives better.</li>
  </ul>
  <a class="btn" href="#" style="left:625px;top:1134px">READ MORE</a>
</section>

<section class="services">
  <h2 class="section-title">What We Do</h2>
  <p class="section-lead">We live and breathe direct response marketing.<br>We are masters of direct response marketing. Our expertise is three folded</p>
  <svg class="service-link" viewBox="0 0 480 10">
    <line x1="0" y1="5" x2="480" y2="5" stroke="#fff" stroke-width="1.5"/>
    <circle cx="17" cy="5" r="4" fill="var(--blue)" stroke="#fff" stroke-width="1.5"/>
    <circle cx="463" cy="5" r="4" fill="var(--blue)" stroke="#fff" stroke-width="1.5"/>
  </svg>
  <div class="service-icon" style="left:166px">
    <span><svg width="60" height="60" viewBox="0 0 60 60"><rect x="6" y="12" width="42" height="32" rx="3" fill="#35aee2"/><rect x="6" y="12" width="42" height="7" fill="#1f8fc8"/><rect x="12" y="26" width="20" height="4" fill="#fff"/><rect x="12" y="34" width="14" height="4" fill="#fff"/><circle cx="46" cy="42" r="9" fill="#1f8fc8" stroke="#fff" stroke-width="2"/></svg></span>
  </div>
  <div class="service-icon" style="left:527px">
    <span><svg width="60" height="60" viewBox="0 0 60 60"><rect x="12" y="8" width="34" height="44" rx="3" fill="#35aee2"/><rect x="18" y="18" width="22" height="3" fill="#fff"/><rect x="18" y="26" width="22" height="3" fill="#fff"/><rect x="18" y="34" width="14" height="3" fill="#fff"/><path d="M40 46l10-14 4 3-10 14-5 1z" fill="#1f8fc8"/></svg></span>
  </div>
  <div class="service-icon" style="left:886px">
    <span><svg width="60" height="60" viewBox="0 0 60 60"><rect x="14" y="8" width="34" height="40" rx="3" fill="#35aee2"/><circle cx="28" cy="30" r="11" fill="#fff" stroke="#1f8fc8" stroke-width="4"/><path d="M20 40l-10 12" stroke="#1f8fc8" stroke-width="6" stroke-linecap="round"/></svg></span>
  </div>
  <p class="service-text" style="left:88px">We create and aggregate great information products.</p>
  <p class="service-text" style="left:449px">We write content that compels people to act.</p>
  <p class="service-text" style="left:808px">We do deep research to offer simple quick and easy solutions to people's most serious problems.</p>
</section>

<section class="team" role="img" aria-label="Photo of the team collaborating around laptops in an office">
  <h2 class="section-title">Our Team &amp; Values</h2>
  <p class="section-lead">We're a small team of smart, funny hard-working specialists who are pushing to become the #1 company in self-reliance. High ambition, radical honesty and a result-oriented mindset are encouraged at BrightLeaf.</p>
  <div class="team-grid">
    <div class="grid-line" style="left:344px;top:0;width:1px;height:290px"></div>
    <div class="grid-line" style="left:705px;top:0;width:1px;height:290px"></div>
    <div class="grid-line" style="left:0;top:134px;width:1046px;height:1px"></div>
    <div class="value-cell" style="left:0;top:26px"><h3>Impact</h3><p>leverage, maximum results, 80/20, greatness</p></div>
    <div class="value-cell" style="left:344px;top:26px"><h3>Ownership</h3><p>leaders must own everything in their world. There is no one else to blame."</p></div>
    <div class="value-cell" style="left:697px;top:26px"><h3>Team spirit</h3><p>cooperation and complementarity, synergy, yin &amp; yang</p></div>
    <div class="value-cell" style="left:0;top:192px"><h3>Courage</h3><p>feel the fear and do it anyway</p></div>
    <div class="value-cell" style="left:344px;top:192px"><h3>Innovation mindset</h3><p>you recombine and reconnect things, so you can solve old problems in new, better ways</p></div>
    <div class="value-cell" style="left:697px;top:192px"><h3>Wisdom</h3><p>learning mode "on", practice of self-improvement as a lifestyle</p></div>
  </div>
</section>

<section class="leaders">
  <div class="leader-photo" role="img" aria-label="Portrait photo of Dorin Vale" style="left:78px;top:2420px"></div>
  <span class="leader-name" style="left:201px;top:2436px">Dorin Vale</span>
  <span class="leader-role" style="left:201px;top:2473px">CEO BrightLeaf</span>
  <p class="leader-bio" style="left:78px;top:2530px">Dorin started or was involved in 15 failed businesses before discovering online copywriting. After that, he ended up writing for Norvix Inc. and did 10-12 "successful" projects there, at least 3 of which broke the million-dollar mark. He wrote the famous HearthPower, and the infamous VoltSecret and Harlan Motor sales letters.</p>
  <a class="btn" href="#" style="left:78px;top:2675px">READ MORE</a>

  <div class="leader-photo" role="img" aria-label="Portrait photo of Mihai Vale" style="left:623px;top:2420px;background:radial-gradient(circle at 50% 40%,#d8c1a8 0%,#5e4a3c 55%,#1e2a36 100%)"></div>
  <span class="leader-name" style="left:746px;top:2436px">Mihai Vale</span>
  <span class="leader-role" style="left:746px;top:2473px">Cofounder &amp; Affiliate Manager BrightLeaf</span>
  <p class="leader-bio" style="left:625px;top:2530px">Since the company's late 2012 start, Mihai grew a network of 5000 affiliates, that dominates ClickVault's survival niche – 3 out of top 5 products are BrightLeaf offers, under the Prepwise brand. He currently oversees sales of $10 million / year, management of a 160k+ email list, marketing,business development and human resources...</p>
  <a class="btn" href="#" style="left:625px;top:2675px">READ MORE</a>
</section>

<section class="contact">
  <div class="contact-card">
    <h3>Contact Details</h3>
    <div class="contact-row" style="top:94px">
      <svg width="16" height="22" viewBox="0 0 16 22"><path d="M8 0a8 8 0 0 0-8 8c0 6 8 14 8 14s8-8 8-14a8 8 0 0 0-8-8zm0 11a3 3 0 1 1 0-6 3 3 0 0 1 0 6z" fill="#fff"/></svg>
      <span>Strada Lalelelor 42,<br>Cluj 400112</span>
    </div>
    <div class="contact-row" style="top:160px">
      <svg width="16" height="18" viewBox="0 0 16 18"><path d="M3 1l3 0 1 4-2 2c1 2 3 4 5 5l2-2 4 1v3c0 1-1 2-2 2C7 16 1 10 1 3c0-1 1-2 2-2z" fill="#fff"/></svg>
      <span>555 014 2291</span>
    </div>
    <div class="contact-row" style="top:198px">
      <svg width="18" height="14" viewBox="0 0 18 14"><rect x="1" y="1" width="16" height="12" fill="none" stroke="#fff" stroke-width="1.6"/><path d="M1 1l8 7 8-7" fill="none" stroke="#fff" stroke-width="1.6"/></svg>
      <span>info@brightleaf.com</span>
    </div>
  </div>
  <h2>Contact Us</h2>
  <div class="field" style="left:450px;top:132px;width:281px;height:41px">Name</div>
  <div class="field" style="left:450px;top:184px;width:281px;height:41px">Email</div>
  <div class="field" style="left:450px;top:236px;width:281px;height:41px">Phone</div>
  <div class="field" style="left:744px;top:132px;width:302px;height:145px">Message</div>
  <div class="send"><svg width="26" height="26" viewBox="0 0 26 26"><path d="M2 12L24 2 17 24 12 15z" fill="#35aee2"/><path d="M12 15L24 2" stroke="#fff" stroke-width="1.5"/></svg></div>
</section>

<footer class="site-footer">©brightleaf- 2018. All Rights Reserved.</footer>

</body>
</html>
```